Breakfast Cafe - The Sunny Perch

It is for my breakfast and lunch cafe with a hawaiian / beach theme. I am open 7 days a week from 7am to 2pm. We serve traditional American food such as omelettes, pancakes, burgers and sandwiches. I'll upload my old card and my new logo to be used. We have a lot of day to day regulars who eat there during the week, our t-shirts actually say 'Locals Only' on them. Hope this helps. Thanks.

Target Market(s)

anyone who has an appetite!

Industry/Entity Type

American Restaurant

Contact Information for Business Card

7340D Marlin Harbor Road
Long Beach, California
(555) 317-2286

Requirements
Must have
• Address and phone number easily readable.
Nice to have
• beach or tropical theme

```html
<!DOCTYPE html>
<html lang="en">
<head>
<meta charset="utf-8">
<title>The Sunny Perch – Business Card</title>
<link rel="stylesheet" href="https://fonts.googleapis.com/css2?family=Baloo+2:wght@600&family=Oswald:wght@400&display=swap">
<style>
  :root {
    --page-bg: #e9e9ea;
    --teal-deep: #1fa792;
    --teal-mid: #3bb394;
    --teal-leaf: #2f9e84;
    --mint-light: #7cc895;
    --white: #ffffff;
    --butter: #f7ee8c;
    --wood: #8a4f22;
    --sky-blue: #5cc4e2;
  }
  html, body {
    margin: 0;
    width: 1200px;
    height: 1019px;
    overflow: hidden;
    background: var(--page-bg);
  }
  .business-card {
    position: absolute;
    left: 100px;
    top: 224px;
    width: 1000px;
    height: 571px;
    overflow: hidden;
  }
  .card-pattern {
    position: absolute;
    inset: 0;
    background:
      radial-gradient(circle 70px at 60px 60px, rgba(47,158,132,0.55), transparent 100%),
      radial-gradient(circle 80px at 380px 20px, rgba(47,158,132,0.45), transparent 100%),
      radial-gradient(circle 80px at 640px 10px, rgba(47,158,132,0.45), transparent 100%),
      radial-gradient(circle 70px at 950px 40px, rgba(47,158,132,0.5), transparent 100%),
      radial-gradient(circle 80px at 960px 260px, rgba(47,158,132,0.5), transparent 100%),
      radial-gradient(circle 70px at 40px 300px, rgba(47,158,132,0.5), transparent 100%),
      radial-gradient(circle 80px at 60px 520px, rgba(47,158,132,0.5), transparent 100%),
      radial-gradient(circle 70px at 520px 560px, rgba(47,158,132,0.45), transparent 100%),
      radial-gradient(circle 70px at 790px 560px, rgba(47,158,132,0.45), transparent 100%),
      radial-gradient(circle 70px at 960px 520px, rgba(47,158,132,0.5), transparent 100%),
      radial-gradient(ellipse 70% 85% at 58% 55%, var(--mint-light) 0%, var(--mint-light) 45%, var(--teal-mid) 78%, var(--teal-deep) 100%);
  }
  .brand-mark {
    position: absolute;
    left: 95px;
    top: 40px;
    width: 340px;
    height: 340px;
    border-radius: 50%;
    background: var(--wood);
  }
  .brand-name {
    position: absolute;
    left: 0;
    width: 530px;
    top: 392px;
    margin: 0;
    text-align: center;
    font-family: "Oswald", sans-serif;
    font-weight: 400;
    font-size: 62px;
    line-height: 1.1;
    color: var(--sky-blue);
  }
  .contact-block {
    position: absolute;
    left: 470px;
    width: 508px;
    top: 112px;
    text-align: center;
  }
  .address {
    margin: 0;
    font-family: "Oswald", sans-serif;
    font-size: 40px;
    line-height: 50px;
    color: var(--white);
  }
  .phone {
    margin: 14px 0 0;
    font-family: "Oswald", sans-serif;
    font-size: 54px;
    line-height: 64px;
    color: var(--white);
  }
  .hours {
    margin: 42px 0 0;
    font-family: "Baloo 2", sans-serif;
    font-weight: 600;
    font-size: 36px;
    line-height: 48px;
    color: var(--butter);
  }
  .tagline {
    margin: 18px 0 0;
    font-family: "Baloo 2", sans-serif;
    font-weight: 600;
    font-size: 28px;
    line-height: 34px;
    color: var(--butter);
  }
</style>
</head>
<body>
  <div class="business-card">
    <div class="card-pattern" role="img" aria-label="Tropical hibiscus leaf pattern on a teal to mint gradient"></div>
    <div class="brand-mark"></div>
    <p class="brand-name">The Sunny Perch</p>
    <div class="contact-block">
      <p class="address">7340D Marlin Harbor Road<br>Long Beach, California</p>
      <p class="phone">(555) 317-2286</p>
      <p class="hours">Breakfast and Lunch<br>7am-2pm Daily</p>
      <p class="tagline">FAMILY OWNED &amp; OPERATED!</p>
    </div>
  </div>
</body>
</html>
```